AMEND EXISTING CAN 250ml

Hi,

Attached you have got the file for an energy drink 250ml can LUMENTIDE, I need to add the logo RQVT attached with the text TECHNICAL SPONSOR and also add the image of the file of the player attached, the photo of the player can be cut, reduced etc..... as you wish basically we need to see the face of the player with his T-shirt uniform.

The can has got a mirror effect with the Lumentide mood and you can check the website www.gofarlumentra.example to better understand, so try to design and play with the same mood.

So, you need to add the logo + text and the image of the player in a nice way without compromising too much the design of LUMENTIDE.

We need a render 3D of the can in PDF or JPEG.

```html
<!DOCTYPE html>
<html lang="en">
<head>
<meta charset="utf-8">
<title>Lumentide 250ml can wrap – Technical Sponsor edition</title>
<link rel="stylesheet" href="https://fonts.googleapis.com/css2?family=Michroma&family=Saira+Semi+Condensed:wght@600&display=swap">
<style>
  :root {
    --stage: #e9eaec;
    --mirror-light: #ffffff;
    --mirror-mid: #eef0f2;
    --mirror-edge: #cfd2d6;
    --mist-blue: #a9c4de;
    --wordmark-grey: #9c9ea2;
    --sponsor-grey: #707276;
    --sponsor-navy: #233463;
    --player-deep: #1c2a45;
    --player-mid: #4f6f96;
  }
  html, body {
    margin: 0;
    width: 1200px;
    height: 904px;
    overflow: hidden;
    background: var(--stage);
  }
  .can-wrap {
    position: absolute;
    left: 430px;
    top: 52px;
    width: 340px;
    height: 800px;
    overflow: hidden;
    background:
      radial-gradient(ellipse 140% 30% at 50% 84%, rgba(169,196,222,0.55), rgba(169,196,222,0) 70%),
      linear-gradient(90deg, var(--mirror-edge) 0%, var(--mirror-mid) 12%, var(--mirror-light) 40%, var(--mirror-light) 62%, var(--mirror-mid) 88%, var(--mirror-edge) 100%);
  }
  .player-photo {
    position: absolute;
    left: 0;
    top: 470px;
    width: 205px;
    height: 330px;
    background:
      linear-gradient(180deg, rgba(79,111,150,0) 0%, rgba(79,111,150,0.55) 30%, var(--player-deep) 75%, var(--player-deep) 100%);
  }
  .label-art {
    position: absolute;
    inset: 0;
  }
  .sponsor-name {
    font-family: "Saira Semi Condensed", sans-serif;
    font-weight: 600;
    font-size: 24px;
    fill: var(--sponsor-navy);
    letter-spacing: 1px;
  }
  .sponsor-caption {
    font-family: "Saira Semi Condensed", sans-serif;
    font-weight: 600;
    font-size: 21px;
    fill: var(--sponsor-grey);
    letter-spacing: 1.5px;
  }
  .wordmark {
    font-family: "Michroma", sans-serif;
    font-size: 80px;
    fill: var(--wordmark-grey);
  }
  .registered {
    font-family: "Michroma", sans-serif;
    font-size: 14px;
    fill: var(--wordmark-grey);
  }
</style>
</head>
<body>
  <main class="can-wrap">
    <div class="player-photo" role="img" aria-label="Photo of the team player, number 18, in his home hockey jersey against an ice arena backdrop"></div>
    <svg class="label-art" width="340" height="800" viewBox="0 0 340 800">
      <g class="sponsor-lockup">
        <circle cx="60" cy="108" r="15" fill="var(--sponsor-navy)"/>
        <text class="sponsor-name" x="82" y="117">RQVT</text>
        <text class="sponsor-caption" transform="translate(104 340) rotate(-90)">TECHNICAL</text>
        <text class="sponsor-caption" transform="translate(127 340) rotate(-90)">SPONSOR</text>
      </g>
      <g class="brand-wordmark">
        <text class="wordmark" transform="translate(282 775) rotate(-90)" textLength="700" lengthAdjust="spacingAndGlyphs">LUMENTIDE</text>
        <text class="registered" transform="translate(232 62) rotate(-90)">®</text>
      </g>
    </svg>
  </main>
</body>
</html>
```